Sydney based Property Management Company need a promotional Flyer design.

We need a flyer, double sided and A4 for our business based in Sydney Australia. The name of the business is 'Larkstone Realty''. We are a professional property management company.
The flyer is to attract business for our property management division. It is aimed at those owning investment properties.
Our flyer needs to professional, clean, easy to read and be an effective sales tool. It needs to communicate that we are experienced, reliable, trustworthy and friendly.
The logo colours are charcoal and grey (please see attached logo). Refer to website www.larkstonerealty.com.au for theme colours.
We have attached a word document with the required copy.
We have also attached images that may be used.
Updates
I have added a few more images with higher resolution photos. I have also have added an example brochure front cover that has a clean uncluttered design for ideas.
A pdf version of the flyer copy has been added.
Property Management

```html
<!DOCTYPE html>
<html lang="en">
<head>
<meta charset="utf-8">
<title>Larkstone Realty – Property Management Flyer</title>
<link rel="stylesheet" href="https://fonts.googleapis.com/css2?family=Open+Sans:ital,wght@0,400;0,600;0,700;1,400;1,700&family=Libre+Baskerville:ital,wght@0,400;0,700;1,700&display=swap">
<style>
:root{
  --backdrop:#cfcfcf;
  --paper:#ffffff;
  --charcoal:#1d1d1d;
  --ink:#333333;
  --grey-text:#6a6a6a;
  --panel:#ececec;
  --quote-box:#8e8f93;
  --green:#4e9a3a;
  --grass:#5f8f3a;
  --serif:'Libre Baskerville',Georgia,serif;
  --sans:'Open Sans',Arial,sans-serif;
}
*{box-sizing:border-box;margin:0;padding:0}
html,body{width:1200px;height:873px;overflow:hidden}
body{background:var(--backdrop);position:relative;font-family:var(--sans);color:var(--ink)}
.page{position:absolute;top:37px;width:570px;height:803px;background:var(--paper);overflow:hidden;box-shadow:0 1px 4px rgba(0,0,0,.2)}
.page--front{left:27px}
.page--back{left:612px}
.abs{position:absolute}
.wordmark{font-family:var(--serif);color:var(--charcoal);font-weight:400;white-space:nowrap}

/* front */
.front-logo{left:0;width:100%;top:28px;text-align:center;font-size:26px;letter-spacing:.5px}
.hero-photo{left:0;top:86px;width:100%;height:349px;background:radial-gradient(ellipse at 50% 60%,#8fb45a,var(--grass) 60%,#3f6a26)}
.hero-offer{left:20px;top:335px;width:530px;height:54px;background:rgba(255,255,255,.85);font-family:var(--serif);font-size:23px;color:var(--charcoal);text-align:center;line-height:54px;white-space:nowrap}
.switch-banner{left:27px;top:462px;width:518px;height:84px}
.switch-dark{left:0;top:0;width:250px;height:84px;background:var(--charcoal);color:#fff;padding:15px 0 0 15px}
.switch-dark h3{font-size:16px;font-weight:400;letter-spacing:.2px;white-space:nowrap}
.switch-dark p{font-size:10px;line-height:13px;margin-top:2px;color:#ddd;white-space:nowrap}
.switch-green{left:229px;top:0;width:289px;height:84px;background:var(--green);color:#fff;clip-path:polygon(0 0,100% 0,100% 100%,0 100%,21px 50%);padding:17px 0 0 36px}
.switch-green h3{font-size:17px;font-weight:400;white-space:nowrap}
.switch-green h3 b{font-weight:700}
.switch-green p{font-size:9px;font-weight:600;margin-top:4px;white-space:nowrap}
.experience{left:0;width:100%;top:574px;text-align:center;font-style:italic;font-weight:700;font-size:13px;line-height:17px;color:var(--charcoal)}
.benefits-intro{left:0;width:100%;top:612px;text-align:center;font-size:13.5px}
.benefit{top:650px;width:140px;text-align:center}
.benefit-icon{display:block;margin:0 auto;width:58px;height:58px;border-radius:50%;border:2px solid var(--green)}
.benefit-label{margin-top:12px;font-family:var(--serif);font-weight:700;font-size:10.5px;line-height:13px;color:var(--charcoal);white-space:nowrap}
.footer{left:0;bottom:0;width:100%;height:38px;background:var(--charcoal);color:#fff;font-size:9.5px;line-height:38px;text-align:center;word-spacing:1px;white-space:nowrap}
.footer span{margin:0 6px}

/* back */
.back-header{left:0;top:0;width:100%;height:75px}
.back-logo{left:68px;top:28px;font-size:16.5px;letter-spacing:0}
.back-divider{left:282px;top:22px;width:1px;height:32px;background:#999}
.back-title{left:296px;top:27px;font-family:var(--serif);font-size:17px;letter-spacing:1.5px;color:var(--charcoal);white-space:nowrap}
.case-panel{left:0;top:75px;width:100%;height:246px;background:var(--panel)}
.case-divider{left:283px;top:92px;width:1px;height:206px;background:#d2d2d2}
.case{top:103px;width:240px}
.case h4{font-size:10.5px;font-weight:700;line-height:13px;color:var(--charcoal);white-space:nowrap}
.case p{font-size:9px;font-style:italic;line-height:11.5px;color:var(--grey-text);text-align:justify;margin-top:8px}
.case p.place{font-style:normal;font-weight:700;color:var(--charcoal);margin-top:8px}
.case-photo{top:212px;width:118px;height:80px;border:2px solid #fff}
.director{left:26px;top:353px;width:418px;font-size:10px;font-style:italic;line-height:12px;color:var(--ink);text-align:justify}
.director b{font-weight:700}
.director-portrait{left:462px;top:346px;width:70px;height:70px;border-radius:50%;border:2px solid #2b4a8a;background:linear-gradient(#dfe4ea,#b9c1cb)}
.testimonial{top:438px;width:234px;height:102px;background:var(--quote-box);color:#fff;font-style:italic;font-size:8.6px;line-height:11.5px;padding:10px 16px;text-align:justify}
.testimonial::after{content:"";position:absolute;bottom:-8px;border:8px solid transparent;border-top-color:var(--quote-box);border-bottom:0}
.testimonial--left::after{left:8px}
.testimonial--right::after{right:8px}
.attribution{top:555px;font-family:var(--serif);font-style:italic;font-weight:700;font-size:12px;color:var(--charcoal);white-space:nowrap}
.call-banner{left:23px;top:603px;width:520px;height:58px;background:var(--green);color:#fff}
.call-divider{left:75px;top:10px;width:1px;height:38px;background:rgba(255,255,255,.6)}
.call-text{left:102px;top:5px;font-family:var(--serif);font-size:19.5px;line-height:24px;white-space:nowrap}
.call-text b{font-weight:700}
.skyline{left:0;top:661px;width:100%;height:104px;background:linear-gradient(#ffffff 0%,#3c5da0 30%,#233668 70%,#1a2440)}
</style>
</head>
<body>

<section class="page page--front">
  <div class="abs wordmark front-logo">LARKSTONE REALTY</div>
  <div class="abs hero-photo" role="img" aria-label="Model houses on green grass with open hands holding a white paper house"></div>
  <div class="abs hero-offer">“<b>FREE</b> property management for 2 months!”</div>

  <div class="abs switch-banner">
    <div class="abs switch-dark">
      <h3>MAKING A CHANGE IS EASY!</h3>
      <p>We contact your current property manager on<br>your behalf, with no inconvenience to you.</p>
    </div>
    <div class="abs switch-green">
      <h3>TODAY on <b>1300-555-190</b></h3>
      <p>Change to Larkstone Realty Management specialists</p>
    </div>
  </div>

  <p class="abs experience">For over 10 years Daniel Marsh and his team have been looking after property<br>investors throughout Sydney.</p>
  <p class="abs benefits-intro">As a Larkstone Realty client your benefits will include:</p>

  <div class="abs benefit" style="left:28px">
    <span class="benefit-icon" role="img" aria-label="Stack of coins shaped like a house" style="background:#f2e3c8"></span>
    <p class="benefit-label">OPTIMAL<br>RENT!</p>
  </div>
  <div class="abs benefit" style="left:146px">
    <span class="benefit-icon" role="img" aria-label="Cash flow road sign" style="background:#9fc6e8"></span>
    <p class="benefit-label">REDUCE REPAIRS &amp;<br>MAINTENANCE BILLS!</p>
  </div>
  <div class="abs benefit" style="left:266px">
    <span class="benefit-icon" role="img" aria-label="House with repair tools" style="background:#e6edf3"></span>
    <p class="benefit-label">REDUCED<br>VACANCY!</p>
  </div>
  <div class="abs benefit" style="left:387px">
    <span class="benefit-icon" role="img" aria-label="Leased stamp over a floor plan" style="background:#f1dede"></span>
    <p class="benefit-label">LEASE YOUR<br>PROPERTY FASTER!</p>
  </div>

  <footer class="abs footer">Ph: 1300 555 190<span>•</span>info@larkstonerealty.com.au<span>•</span>www.larkstonerealty.com.au<span>•</span>www.fb.com/LarkstoneRealty</footer>
</section>

<section class="page page--back">
  <header class="abs back-header">
    <div class="abs wordmark back-logo">LARKSTONE REALTY</div>
    <div class="abs back-divider"></div>
    <div class="abs back-title">CASE STUDIES</div>
  </header>

  <div class="abs case-panel"></div>
  <div class="abs case-divider"></div>

  <article class="abs case" style="left:26px">
    <h4>OUR EXPERIENCE REDUCES CLIENTS<br>PLUMBING BILL BY 50%</h4>
    <p class="place">- Marayong</p>
    <p>We managed to reduce the clients plumbing bill by $800 by coordinating an excavator to unearth a problem pipe. This solution was both time and cost effective.</p>
  </article>
  <div class="abs case-photo" style="left:24px;background:linear-gradient(#7a5a3a,#a0724a)" role="img" aria-label="Empty living room with timber floors"></div>
  <div class="abs case-photo" style="left:144px;background:linear-gradient(#b8c8d8 35%,#5c8a3a 60%)" role="img" aria-label="Backyard lawn behind the house"></div>

  <article class="abs case" style="left:302px">
    <h4>SMART CHANGES TO A UNIT INCREASE ITS<br>RENTABILITY</h4>
    <p class="place">- Bondi</p>
    <p>A smart solution to a water heating issue and minor renovations to the kitchen, see a Bondi unit leased in low season faster than comparable units on the rental market.</p>
  </article>
  <div class="abs case-photo" style="left:300px;background:linear-gradient(#e4e6e8,#b8bcc0)" role="img" aria-label="Renovated unit kitchen"></div>
  <div class="abs case-photo" style="left:420px;background:linear-gradient(#e8e8e6 60%,#8a5a32)" role="img" aria-label="Unit interior with timber floor"></div>

  <p class="abs director"><b>Daniel Marsh</b> is Larkstone Realty’s director. He is a respected industry professional with 25 years’ experience in Property and Finance. Daniel draws on his experience in property inspections and purchases as well as building and construction and finance to help his clients save money and time.</p>
  <div class="abs director-portrait" role="img" aria-label="Portrait of the director"></div>

  <blockquote class="abs testimonial testimonial--left" style="left:24px">“Daniel found the ideal investment property for us. He also coordinated the renovation which provided us with a substantial increase in rent. He now manages all of our properties. Whist we were both working overseas it was imperative that we had someone looking after our properties that we could trust.”</blockquote>
  <blockquote class="abs testimonial testimonial--right" style="left:282px">“Daniel has been providing us with advice and guidance on our property portfolio since 2006. The team at Larkstone Realty do a lot more than collect rent and manage tenants. They have helped us increase the value of our properties through coordination of renovations, maximising the rent and reducing the repairs and maintenance costs.”</blockquote>
  <p class="abs attribution" style="left:34px">Graham and Lucy Prentice</p>
  <p class="abs attribution" style="right:37px">Kostas Family Super Fund</p>

  <div class="abs call-banner">
    <svg class="abs" style="left:24px;top:14px" width="30" height="30" viewBox="0 0 24 24" aria-hidden="true"><path fill="#fff" d="M6.6 10.8c1.4 2.8 3.8 5.1 6.6 6.6l2.2-2.2c.3-.3.7-.4 1-.2 1.1.4 2.3.6 3.6.6.6 0 1 .4 1 1V20c0 .6-.4 1-1 1C10.6 21 3 13.4 3 4c0-.6.4-1 1-1h3.5c.6 0 1 .4 1 1 0 1.3.2 2.5.6 3.6.1.3 0 .7-.2 1L6.6 10.8z"/></svg>
    <div class="abs call-divider"></div>
    <p class="abs call-text"><b>Call us today</b> to take advantage of our<br>limited special offer <b>on 1300 555 190!</b></p>
  </div>
  <div class="abs skyline" role="img" aria-label="Sydney harbour skyline at dusk"></div>

  <footer class="abs footer">Ph: 1300 555 190<span>•</span>info@larkstonerealty.com.au<span>•</span>www.larkstonerealty.com.au<span>•</span>www.fb.com/LarkstoneRealty</footer>
</section>

</body>
</html>
```